Stationery For Upscale Concierge Company

Create stationary that looks good in black and white and uses the attached logo. Needs to be upscale using upscale fonts and layout. Use the attached logo. Reverse out if necessary.

```html
<!DOCTYPE html>
<html lang="en">
<head>
<meta charset="utf-8">
<title>Harbor Lane — Business Cards</title>
<link href="https://fonts.googleapis.com/css2?family=Cinzel:wght@400&family=Open+Sans:wght@400;700&display=swap" rel="stylesheet">
<style>
  :root {
    --canvas: #e9e7e4;
    --card-black: #121212;
    --card-white: #ffffff;
    --ink: #111111;
    --ink-soft: #3a3a3a;
    --foil: #8d8d8d;
    --rule: #2a2a2a;
  }
  * { margin: 0; padding: 0; box-sizing: border-box; }
  html, body {
    width: 1200px; height: 1200px; overflow: hidden;
    background: var(--canvas);
  }
  .sheet {
    position: relative; width: 1200px; height: 1200px;
  }
  .card {
    position: absolute; left: 170px;
    width: 860px; height: 491px;
    box-shadow: 0 6px 18px rgba(0,0,0,0.18);
  }
  .card--front { top: 80px; background: var(--card-black); }
  .card--back { top: 629px; background: var(--card-white); }

  .brand {
    font-family: "Cinzel", serif;
    font-weight: 400;
    letter-spacing: 0.04em;
    white-space: nowrap;
    display: flex; align-items: center; gap: 18px;
  }
  .brand__mark {
    width: 14px; height: 14px; border-radius: 50%;
  }
  .card--front .brand {
    position: absolute; left: 0; right: 0; top: 0; bottom: 0;
    justify-content: center;
    font-size: 64px; color: var(--foil);
  }
  .card--front .brand__mark { background: var(--foil); }

  .card--back .brand {
    position: absolute; left: 60px; top: 210px;
    font-size: 40px; color: var(--ink);
  }
  .card--back .brand__mark { background: var(--ink); width: 10px; height: 10px; }

  .divider {
    position: absolute; left: 470px; top: 110px;
    width: 2px; height: 270px; background: var(--rule);
  }
  .contact {
    position: absolute; left: 510px; top: 118px;
    font-family: "Open Sans", sans-serif; color: var(--ink);
  }
  .contact__name { font-weight: 700; font-size: 32px; line-height: 1.1; }
  .contact__title { font-size: 19px; color: var(--ink-soft); margin-bottom: 20px; }
  .contact__address { font-size: 21px; line-height: 1.3; margin-bottom: 14px; color: var(--ink-soft); }
  .contact__line {
    display: flex; align-items: center; gap: 10px;
    font-size: 21px; line-height: 1.45; color: var(--ink-soft);
  }
  .contact__icon { width: 16px; height: 16px; flex: none; }
</style>
</head>
<body>
<main class="sheet">
  <section class="card card--front" aria-label="Card front">
    <div class="brand"><span class="brand__mark"></span>Harbor Lane</div>
  </section>

  <section class="card card--back" aria-label="Card back">
    <div class="brand"><span class="brand__mark"></span>Harbor Lane</div>
    <div class="divider"></div>
    <div class="contact">
      <p class="contact__name">Adrian Cole</p>
      <p class="contact__title">President</p>
      <p class="contact__address">48 Linden Avenue, Suite 200,<br>10012,&nbsp; Country</p>
      <p class="contact__line">
        <svg class="contact__icon" viewBox="0 0 16 16"><path fill="#111" d="M3.6 1.2l2.3 2.6-1.3 1.8c.9 2.1 2.6 3.8 4.7 4.7l1.8-1.3 2.6 2.3-1.5 2.4C6.6 13.5 2.5 9.4 1.2 3.8z"/></svg>
        (555) 014-2290
      </p>
      <p class="contact__line">
        <svg class="contact__icon" viewBox="0 0 16 16"><rect x="1" y="3" width="14" height="10" fill="#111"/><path d="M1.5 3.5L8 9l6.5-5.5" fill="none" stroke="#fff" stroke-width="1.3"/></svg>
        hello@harborlane.com
      </p>
      <p class="contact__line">
        <svg class="contact__icon" viewBox="0 0 16 16"><circle cx="8" cy="8" r="7" fill="#111"/><path d="M1 8h14M8 1c-3 3.5-3 10.5 0 14M8 1c3 3.5 3 10.5 0 14" fill="none" stroke="#fff" stroke-width="1"/></svg>
        www.harborlane.com
      </p>
    </div>
  </section>
</main>
</body>
</html>
```